Legal and business training card design

We need a business card design for KOBAN - Coastal Workplace Advisory and Skills Bureau a new company set up in county Victoria . Our aim is to assist regional business with their every day employment law legal issues and questions - this would include compliance within the workplace, employment conts, EBAs, dismissals, and general OHS. As well as KOBAN will engage in training in particular Human Resources, management v leadership, time management , as well as constructing training around individual business/s needs. So we are multi purpose.
Our product is our service. It's designed specifically for regional base business hence we understand the requirements and needs of regional business v city business. At the same time the card must be simple, yet hard hitting, getting the message across in a couple of seconds.
I would like to see red and yellows, with perhaps a symbol/logo that represents the regional areas incorporated into the KOBAN name ie curvy R in which the R's " right leg "expands under the entire acronym. Or you may have some better ideas. I also like the symbol of the square/s to match our slogan "Shaping workplace answers beyond the usual limits".
Thanks
Industry/Entity Type
Training
Contact Information for Business Card
KOBAN
Coastal Workplace Advisory & Skills Bureau
"Shaping workplace answers beyond the usual limits"
Megan Thorley B.A LL.B
Director and Principal
T: 1800 472 918 E: megan@kobanhq.com.au
W: www.kobanhq.com.au

```html
<!DOCTYPE html>
<html lang="en">
<head>
<meta charset="utf-8">
<title>KOBAN – Business Card</title>
<link rel="stylesheet" href="https://fonts.googleapis.com/css2?family=Roboto:wght@400;500;700&family=Roboto+Condensed:wght@400;700&display=swap">
<style>
  :root {
    --amber: #f0a800;
    --ink: #0d0d0d;
    --paper: #ffffff;
    --stage: #e9e6e1;
  }
  * { margin: 0; padding: 0; box-sizing: border-box; }
  html, body { width: 1200px; height: 848px; overflow: hidden; }
  body {
    background: var(--stage);
    font-family: "Roboto", Arial, sans-serif;
    display: flex;
    align-items: center;
    justify-content: center;
    gap: 40px;
  }
  .card {
    position: relative;
    width: 540px;
    height: 309px;
    overflow: hidden;
    box-shadow: 0 10px 28px rgba(0,0,0,.18);
  }
  .card-art { position: absolute; inset: 0; }

  /* front */
  .card--front { background: var(--paper); }
  .front-mark {
    position: absolute;
    left: 76px; width: 148px;
    top: 130px;
    text-align: center;
    font-family: "Roboto Condensed", Arial, sans-serif;
    font-weight: 700;
    font-size: 44px;
    letter-spacing: 0.5px;
    color: var(--ink);
    line-height: 1;
  }
  .front-info { position: absolute; left: 268px; right: 14px; top: 30px; }
  .company {
    font-family: "Roboto Condensed", Arial, sans-serif;
    font-weight: 700;
    font-size: 21px;
    line-height: 1.02;
    color: var(--amber);
  }
  .tagline {
    margin-top: 3px;
    font-family: "Roboto Condensed", Arial, sans-serif;
    font-size: 11px;
    color: var(--ink);
  }
  .person { margin-top: 44px; }
  .person-name {
    font-family: "Roboto Condensed", Arial, sans-serif;
    font-weight: 700;
    font-size: 27px;
    color: var(--ink);
    line-height: 1;
  }
  .person-role {
    font-family: "Roboto Condensed", Arial, sans-serif;
    font-size: 11px;
    color: var(--ink);
    margin-top: 3px;
  }
  .contacts { list-style: none; margin-top: 26px; }
  .contacts li {
    display: flex; align-items: center; gap: 12px;
    font-family: "Roboto Condensed", Arial, sans-serif;
    font-size: 13.5px; color: var(--ink);
    height: 20px;
  }
  .contacts svg { width: 15px; height: 15px; flex: none; }

  /* back */
  .card--back { background: var(--amber); }
  .back-lockup {
    position: absolute; left: 0; right: 0; top: 96px;
    text-align: center; color: var(--ink);
  }
  .back-mark {
    font-family: "Roboto", Arial, sans-serif;
    font-weight: 700;
    font-size: 66px;
    letter-spacing: 3px;
    line-height: 1;
  }
  .back-name {
    margin-top: 6px;
    font-family: "Roboto", Arial, sans-serif;
    font-weight: 500;
    font-size: 17px;
  }
</style>
</head>
<body>

  <section class="card card--front" aria-label="Business card front">
    <svg class="card-art" viewBox="0 0 540 309" aria-hidden="true">
      <rect x="0" y="0" width="28" height="309" fill="var(--ink)"/>
      <rect x="28" y="0" width="200" height="309" fill="var(--amber)"/>
      <polygon points="0,66 54,86 64,196 36,254 0,254" fill="var(--paper)"/>
      <rect x="228" y="0" width="12" height="309" fill="var(--ink)"/>
    </svg>

    <div class="front-mark">KOBAN</div>

    <div class="front-info">
      <h1 class="company">Coastal Workplace Advisory<br>&amp; Skills Bureau</h1>
      <p class="tagline">"Shaping workplace answers beyond the usual limits"</p>

      <div class="person">
        <p class="person-name">Megan Thorley</p>
        <p class="person-role">B.A LL.B Director and Principal</p>
      </div>

      <ul class="contacts">
        <li>
          <svg viewBox="0 0 16 16" aria-hidden="true"><path d="M3.2 1.5l2.3 2.6-1.2 1.6c.9 2 2.4 3.6 4.4 4.6l1.6-1.2 2.7 2.2-1.4 2.4C6.3 13.2 2.7 9.6 1 4.3z" fill="var(--ink)"/></svg>
          <span>1800 472 918</span>
        </li>
        <li>
          <svg viewBox="0 0 16 16" aria-hidden="true"><rect x="1.5" y="2" width="13" height="9" fill="none" stroke="var(--ink)" stroke-width="1.4"/><rect x="5" y="12.5" width="6" height="1.5" fill="var(--ink)"/></svg>
          <span>www.kobanhq.com.au</span>
        </li>
        <li>
          <svg viewBox="0 0 16 16" aria-hidden="true"><rect x="1" y="3.5" width="14" height="9" fill="var(--ink)"/><path d="M1.5 4l6.5 5 6.5-5" fill="none" stroke="var(--paper)" stroke-width="1.2"/></svg>
          <span>megan@kobanhq.com.au</span>
        </li>
      </ul>
    </div>
  </section>

  <section class="card card--back" aria-label="Business card back">
    <svg class="card-art" viewBox="0 0 540 309" aria-hidden="true">
      <rect x="0" y="281" width="540" height="28" fill="var(--ink)"/>
      <polygon points="300,309 322,262 440,250 470,281 470,309" fill="var(--paper)"/>
    </svg>
    <div class="back-lockup">
      <p class="back-mark">KOBAN</p>
      <p class="back-name">Coastal Workplace Advisory &amp; Skills Bureau</p>
    </div>
  </section>

</body>
</html>
```